Freelance Translator in Need of a Business Card

I am a freelance Japanese to English translator. I work in the video game localization industry and do literary translation in my spare time. I would like to have both the English word 'Translator' and the Japanese '翻訳者' in the job title. The final design should evoke trust, openness, and reliability.

Target Market(s)

Video game localization companies
Japanese comic book artists

Industry/Entity Type

Business

Contact Information for Business Card

Daniel Ostrowik, Translator
dan.ostrowik@quellbox.net
verolingworks.com
twitter: @verol_tx

Colors

Designer to choose colors to be used in the design.

```html
<!DOCTYPE html>
<html lang="en">
<head>
<meta charset="utf-8">
<title>Daniel Ostrowik – Translator Business Card</title>
<link rel="stylesheet" href="https://fonts.googleapis.com/css2?family=Open+Sans:wght@400;700&family=Noto+Sans+JP:wght@400&display=swap">
<style>
  :root {
    --brand-blue: #1670a6;
    --name-blue: #1b6ea6;
    --ink-grey: #4a4a4a;
    --mark-grey: #5e5e5e;
    --card-white: #ffffff;
    --backdrop: #e9e6e2;
  }
  * { margin: 0; padding: 0; box-sizing: border-box; }
  html, body {
    width: 1200px; height: 1000px; overflow: hidden;
    background: var(--backdrop);
    font-family: "Open Sans", "Noto Sans JP", sans-serif;
  }
  .canvas { position: relative; width: 1200px; height: 1000px; }
  .card {
    position: absolute; left: 266px; width: 666px; height: 396px;
    border-radius: 24px; overflow: hidden;
  }
  .card--front { top: 74px; background: var(--brand-blue); }
  .card--back { top: 534px; background: var(--card-white); }

  .front-mark {
    position: absolute; left: 273px; top: 150px; width: 120px; height: 120px;
    border: 6px solid var(--card-white); border-radius: 10px;
  }
  .front-title {
    position: absolute; left: 0; right: 0; top: 282px; text-align: center;
    color: var(--card-white); font-weight: 700; font-size: 27px; letter-spacing: 0.5px;
  }

  .back-mark {
    position: absolute; left: 100px; top: 130px; width: 120px; height: 120px;
    border: 6px solid var(--brand-blue); border-radius: 10px;
  }
  .divider {
    position: absolute; left: 330px; top: 121px; width: 2px; height: 154px;
    background: var(--brand-blue);
  }
  .identity { position: absolute; left: 374px; top: 115px; }
  .identity__name {
    color: var(--name-blue); font-weight: 700; font-size: 19px; letter-spacing: 0.3px;
    line-height: 26px;
  }
  .identity__role {
    color: var(--ink-grey); font-size: 16px; line-height: 22px;
    font-family: "Open Sans", "Noto Sans JP", sans-serif;
  }
  .contacts { position: absolute; left: 374px; top: 199px; list-style: none; }
  .contacts__item {
    display: flex; align-items: center; gap: 6px;
    color: var(--ink-grey); font-size: 16px; line-height: 26px;
  }
  .contacts__item:first-child { margin-bottom: 8px; }
  .contacts__icon { width: 14px; height: 14px; flex: none; }
  .contacts__icon * { fill: none; stroke: var(--brand-blue); stroke-width: 1.6; }
  .contacts__icon .solid { fill: var(--brand-blue); stroke: none; }
</style>
</head>
<body>
<main class="canvas">
  <section class="card card--front" aria-label="Card front">
    <div class="front-mark" aria-hidden="true"></div>
    <p class="front-title">TRANSLATOR</p>
  </section>

  <section class="card card--back" aria-label="Card back">
    <div class="back-mark" aria-hidden="true"></div>
    <div class="divider" aria-hidden="true"></div>
    <div class="identity">
      <p class="identity__name">DANIEL OSTROWIK</p>
      <p class="identity__role">Translator / <span lang="ja">翻訳者</span></p>
    </div>
    <ul class="contacts">
      <li class="contacts__item">
        <svg class="contacts__icon" viewBox="0 0 14 14" aria-hidden="true"><circle class="solid" cx="7" cy="7" r="6"/></svg>
        @verol_tx
      </li>
      <li class="contacts__item">
        <svg class="contacts__icon" viewBox="0 0 14 14" aria-hidden="true"><rect x="1" y="3" width="12" height="8"/><path d="M1 3l6 4.5L13 3"/></svg>
        dan.ostrowik@quellbox.net
      </li>
      <li class="contacts__item">
        <svg class="contacts__icon" viewBox="0 0 14 14" aria-hidden="true"><circle cx="7" cy="7" r="5.5"/><path d="M1.5 7h11M7 1.5c2.5 3 2.5 8 0 11M7 1.5c-2.5 3-2.5 8 0 11"/></svg>
        verolingworks.com
      </li>
    </ul>
  </section>
</main>
</body>
</html>
```